KTR-OB R-Value Adjustment Paper

This is a technical paper needing professional layout that is compatible with our current style guidelines; it will be used in digital and print media. It has numerous tables and graphs.

We have attached a report "KTR Cladding EPD" issued to our company under Marrowfield Assurance graphic design guidelines. While this does NOT reflect our style branding, it does represent the 'technical' presentation we are looking for.

To view our typical company design/style please see our website at www.ktrcouncil.org. Our primary RGB colors are: (187,140,9); (94,47,29); (94,138,164); and (164,167,15). Secondary RGB colors are (249,162,28) and (218,210,208). Our title/header font is DIN Next LT Pro and our copy font is Calibri 10.5 pt. We can deviate from the font specification if beneficial.

The attached file, "KTR-OB Rvalue Adj Factor" is a partial representation of the full document that will need design services. For the concepts we would like to see a cover/title page, a text/copy page and a sample of data graphic treatments.Once we have agreed upon a design concept we will determine full costs to complete the project.

Target Market(s)

Building and construction professionals, architects, building code officials

Font styles to use
Other font styles liked:
• DIN Next LT Pro

Requirements
Must have
• Design elements that help make the information easy to read and use.
Nice to have
• Right amount of white space.

```html
<!DOCTYPE html>
<html lang="en">
<head>
<meta charset="utf-8">
<title>KTR-OB R-Value Adjustment Paper – Aging and Moisture</title>
<link href="https://fonts.googleapis.com/css2?family=Barlow+Condensed:wght@600&family=Carlito:ital,wght@0,400;1,400&display=swap" rel="stylesheet">
<style>
  :root{
    --gold:#bb8c09;
    --brown:#5e2f1d;
    --green:#9bc31c;
    --orange:#f9a21c;
    --grid:#c8c8c8;
    --ink:#1a1a1a;
    --paper:#ffffff;
  }
  html,body{margin:0;padding:0;overflow:hidden;}
  body{width:855px;height:1200px;background:var(--paper);position:relative;
       font-family:'Carlito',Calibri,Arial,sans-serif;color:var(--ink);}
  .section-head{position:absolute;left:25px;right:29px;height:60px;}
  .brand{position:absolute;left:0;top:14px;display:flex;align-items:center;gap:5px;}
  .brand-dot{width:14px;height:14px;border-radius:50%;background:var(--gold);}
  .brand-name{font-family:'Barlow Condensed',sans-serif;font-weight:600;font-size:19px;color:var(--gold);}
  .section-title{position:absolute;left:72px;top:0;margin:0;font-family:'Barlow Condensed',sans-serif;
       font-weight:600;font-size:35px;line-height:44px;color:#000;}
  .section-rule{position:absolute;left:72px;right:0;top:46px;height:4px;background:var(--green);}
  .copy{position:absolute;left:26px;width:806px;font-size:12.6px;line-height:16.6px;}
  .copy p{margin:0 0 16.6px;}
  .copy p.tight{margin:0;}
  .chart{position:absolute;left:0;top:300px;}
  .page-number{position:absolute;left:25px;top:1126px;width:42px;height:42px;border-radius:5px;
       background:var(--green);color:#fff;font-family:'Barlow Condensed',sans-serif;font-weight:600;
       font-size:30px;line-height:42px;text-align:center;}
</style>
</head>
<body>

<header class="section-head" style="top:25px">
  <div class="brand"><span class="brand-dot"></span><span class="brand-name">KTR</span></div>
  <h2 class="section-title">Impact of Aging</h2>
  <div class="section-rule"></div>
</header>

<div class="copy" style="top:123px">
  <p>The FTC’s R-value Rule requires the published R-value of insulation to fully reflect the impact of aging on the insulation. The process of aging causes some insulation to lose its captive blowing agents over time. XPS uses gaseous blowing agents, which initially contribute to better R-values, but, over time, the gases dissipate, causing the R-value of XPS to decrease. In contrast, EPS contains only air, so its R-values do not decrease over time from gaseous exchange.</p>
  <p class="tight">In Canada, XPS manufacturers must publish a long-term thermal resistance (LTTR), which is an estimate of the product’s R-value at five years of age. This is an improvement and a distinction between the insulation’s initial R-value or an R-value determined by a short-term conditioning method. Nonetheless, LTTR does not reflect the full extent of aging over the life of the insulation when used in buildings that are anticipated to have a minimum lifetime of 50 years.</p>
  <p class="tight">Figure 3 shows the R-value for EPS Type II and IX and XPS Type IV and X over time.</p>
</div>

<svg class="chart" width="855" height="500" viewBox="0 300 855 500" font-family="Carlito, Calibri, sans-serif" font-size="13" fill="#1a1a1a">
  <g stroke="var(--grid)" stroke-width="1.2">
    <line x1="152" y1="323" x2="595" y2="323"/><line x1="152" y1="394" x2="595" y2="394"/>
    <line x1="152" y1="466" x2="595" y2="466"/><line x1="152" y1="537" x2="595" y2="537"/>
    <line x1="152" y1="609" x2="595" y2="609"/><line x1="152" y1="680" x2="595" y2="680"/>
    <line x1="152" y1="323" x2="152" y2="680"/><line x1="241" y1="323" x2="241" y2="680"/>
    <line x1="329" y1="323" x2="329" y2="680"/><line x1="418" y1="323" x2="418" y2="680"/>
    <line x1="506" y1="323" x2="506" y2="680"/><line x1="595" y1="323" x2="595" y2="680"/>
  </g>
  <g text-anchor="end">
    <text x="124" y="328">5,5</text><text x="124" y="399">5</text><text x="124" y="471">4,5</text>
    <text x="124" y="542">4</text><text x="124" y="614">3,5</text><text x="124" y="685">3</text>
  </g>
  <g text-anchor="middle">
    <text x="152" y="711">0</text><text x="241" y="711">10</text><text x="329" y="711">20</text>
    <text x="418" y="711">30</text><text x="506" y="711">40</text><text x="595" y="711">50</text>
    <text x="373" y="742">Age, Years</text>
  </g>
  <line x1="152" y1="506" x2="595" y2="506" stroke="var(--orange)" stroke-width="3"/>
  <g fill="var(--orange)"><circle cx="152" cy="506" r="6"/><circle cx="161" cy="506" r="6"/><circle cx="187" cy="506" r="6"/><circle cx="595" cy="506" r="6"/></g>
  <line x1="152" y1="537" x2="595" y2="537" stroke="var(--green)" stroke-width="3"/>
  <g fill="var(--green)"><circle cx="152" cy="537" r="6"/><circle cx="161" cy="537" r="6"/><circle cx="187" cy="537" r="6"/><circle cx="595" cy="537" r="6"/></g>
  <circle cx="152" cy="394" r="6.5" fill="var(--brown)"/>
  <circle cx="196" cy="413" r="6.5" fill="var(--brown)"/>
  <circle cx="196" cy="439" r="6.5" fill="var(--green)"/>
  <line x1="174" y1="417" x2="277" y2="459" stroke="var(--green)" stroke-width="3"/>
  <polygon points="292,466 268,467 276,449" fill="var(--green)"/>
  <line x1="640" y1="430" x2="706" y2="430" stroke="var(--green)" stroke-width="3"/>
  <circle cx="673" cy="430" r="6.5" fill="var(--green)"/>
  <text x="721" y="435">EPS Type II</text>
  <line x1="640" y1="481" x2="706" y2="481" stroke="var(--orange)" stroke-width="3"/>
  <circle cx="673" cy="481" r="6.5" fill="var(--orange)"/>
  <text x="721" y="486">EPS Type IX</text>
  <circle cx="673" cy="532" r="6.5" fill="var(--green)"/>
  <text x="721" y="537">XPS Type X</text>
  <circle cx="673" cy="584" r="6.5" fill="var(--brown)"/>
  <text x="721" y="589">XPS Type X</text>
  <text x="148" y="780" font-style="italic" font-size="12.6">Figure 3. Loss of R-value Over Time for Polystyrene Insulations</text>
</svg>

<header class="section-head" style="top:840px">
  <div class="brand"><span class="brand-dot"></span><span class="brand-name">KTR</span></div>
  <h2 class="section-title">Moisture</h2>
  <div class="section-rule"></div>
</header>

<div class="copy" style="top:911px">
  <p>The R-value of insulation typically is determined under ideal, dry laboratory conditions. In many building applications, polystyrene foam insulation is protected from moisture, and the R-values determined under dry laboratory conditions are appropriate. Examples include insulation under roof membranes and wall insulation covered by a weather-resistive barrier. In these applications, no adjustment to the R-value is needed based on the insulation’s exposure to moisture.</p>
  <p>Polystyrene foam in ground contact applications may be exposed to moisture, and, in such cases, an adjustment to the laboratory R-value based on these conditions is appropriate.</p>
  <p>Under these conditions, the reductions in the R-values of both EPS and XPS materials are well documented in international standard ISO/FDIS 10456 (ISO, 2007) and Figure 4 shows the loss of R-value for EPS and XPS as a function of moisture.</p>
</div>

<div class="page-number">1</div>

</body>
</html>
```